Brightgate Automotive Service Website Design

We are working with Brightgate Automotive Service. They are a local mechanic/garage and in need of a new website design.

Some sites to use for inspiration:

https://www.torvalle.example
https://www.quenby.example
https://parks-carcare.example
https://www.hollowmerefullautocare.example/

Thank you for taking the time to consider designing a website for us. We are web developers based in Stockton, CA, USA. Most of our projects go through the same process. Understanding this process may help you win a project with us. We custom-code all of our websites in-house. We don’t have any requirements as to what tools you use for your design, but we prefer Figma files. For any design that we label as four-stars, we send it to the client for review. The client picks the final design they want us to use. Once we complete this process, we will continue to show additional clients all the four-star sites and purchase them later. Your designs will have multiple chances to sell. For better chances of success, we ask that you follow these guidelines.

IMAGES:
If you use any images or icons in the design, we ask that you have a link to the asset so we can purchase the image/icon. Most of the designs we submit do not have the customer’s images on them unless they have some great images. Be creative; show us the feeling you are trying to portray with your image choices. Use any royalty-free site you choose. We subscribe to Adobe and mainly use their images, but we can purchase images outside of Adobe.

PLEASE NOTE: we will not submit designs to clients with watermarks on the images.

FONTS:
We ask that you identify the fonts used in the design. This can be done in a message if you want. We typically use Google Fonts and Adobe Fonts.

CONTENT:
We're always open to different content and ideas. We often submit designs with stock images so the client can see our vision. We typically take pictures after the website launch to use their images with our vision. Lorem Ipsum is fine for paragraphs, but we ask that you write the headers in correct English. We want to be able to show the vision and identify the sections of the website.

INSPIRATION:
We typically add a couple of links in the brief of websites we like to help you get started in your design.

REVISIONS:
We do not often ask for revisions of the designs unless we see something in the design that may not appeal to the client. If there are slight changes that we want to make, we do that in the development process.

FEEDBACK:
We rarely give feedback on designs during the design process. We are working on many website projects and do not have the time to provide feedback. We usually respond if your request is well thought out and asks specific questions, but a note asking “feedback, please” usually goes unanswered.

```html
<!DOCTYPE html>
<html lang="en">
<head>
<meta charset="utf-8">
<title>Brightgate Automotive Service</title>
<link href="https://fonts.googleapis.com/css2?family=Bebas+Neue&family=Montserrat:ital,wght@0,400;0,500;0,600;0,700;1,400&family=Tinos:wght@700&display=swap" rel="stylesheet">
<style>
:root{
  --red:#c4120f;
  --red-dark:#a50d0b;
  --ink:#151515;
  --dark:#0f0f10;
  --field:#d9d9d9;
  --text:#5a5a5a;
  --white:#ffffff;
  --star:#c9c23c;
}
*{margin:0;padding:0;box-sizing:border-box}
html,body{width:1200px;height:5146px;overflow:hidden;background:var(--white)}
body{position:relative;font-family:'Montserrat',sans-serif;color:var(--ink)}
.abs{position:absolute}
.display{font-family:'Bebas Neue',sans-serif;font-weight:400;letter-spacing:.5px}
.btn{position:absolute;display:flex;align-items:center;justify-content:center;gap:12px;background:var(--red);color:var(--white);font-weight:600;font-size:15px;text-transform:uppercase;letter-spacing:.3px}
.btn svg{width:24px;height:24px}
.photo{position:absolute}

/* top bar */
.topbar{top:0;left:0;width:1200px;height:80px;background:var(--ink)}
.topbar-red{top:0;left:330px;width:870px;height:80px;background:var(--red);clip-path:polygon(40px 0,100% 0,100% 100%,0 100%)}
.brand-top{top:10px;left:40px;font-size:58px;color:#d6d6d6;line-height:60px}
.contact{display:flex;align-items:center;gap:14px;color:var(--white)}
.contact .ico{width:52px;height:52px;border:2px solid var(--white);border-radius:50%;display:flex;align-items:center;justify-content:center;flex:none}
.contact small{display:block;font-size:15px;font-weight:600}
.contact span{font-size:15px;font-weight:500;white-space:nowrap}
.social{top:32px;display:flex;gap:26px;left:1008px}
.social i{display:block;width:20px;height:20px;border-radius:50%;background:var(--white)}

/* nav */
.nav{top:80px;left:0;width:1200px;height:80px;background:var(--white)}
.nav a{position:absolute;top:34px;font-size:13px;font-weight:600;color:var(--ink);text-decoration:none}
.search{position:absolute;left:978px;top:26px;width:170px;height:32px;background:var(--field);font-size:13px;color:#777;display:flex;align-items:center;justify-content:center}

/* hero */
.hero{top:160px;left:0;width:1200px;height:640px;background:linear-gradient(110deg,#0b0b0c 0%,#1e1f22 45%,#4a4a4c 75%,#222 100%);clip-path:polygon(0 0,100% 0,100% 100%,0 93.75%)}
.hero h1{position:absolute;left:64px;top:140px;font-size:68px;line-height:68px;color:var(--white)}
.hero h1 em{font-style:normal;color:var(--red)}
.hero p{position:absolute;left:64px;top:298px;width:490px;font-size:16.5px;line-height:25px;color:var(--white)}

/* quote form */
.quote{top:542px;left:636px;width:434px;height:606px;background:var(--white);border:1px solid #cfcfcf}
.quote-head{height:68px;background:var(--red);color:var(--white);font-size:32px;display:flex;align-items:center;justify-content:center}
.field{position:absolute;left:43px;width:346px;height:50px;background:var(--field);font-size:13px;font-weight:500;color:#555;padding:16px 26px}
.field.area{height:148px}

/* who */
.who h2{position:absolute;left:74px;top:842px;font-size:42px}
.who p{position:absolute;left:74px;top:906px;width:478px;font-size:13px;line-height:19px;color:var(--text)}

/* features */
.feature{position:absolute;top:1240px;width:300px;text-align:center}
.feature svg{width:110px;height:110px}
.feature h3{font-size:31px;margin-top:22px}
.feature p{font-size:13.5px;line-height:19px;color:var(--text);margin:10px auto 0;width:268px}

/* services */
.services{top:1580px;left:0;width:1200px;height:636px;background:linear-gradient(135deg,#0c0c0d 0%,#1b1c1f 40%,#2b2c2f 70%,#0f0f10 100%);clip-path:polygon(0 42px,100% 0,100% 100%,0 100%)}
.kicker{font-size:15px;font-weight:600;color:var(--red);text-transform:uppercase;letter-spacing:.5px}
.sec-title{font-size:40px}
.svc{position:absolute;width:300px}
.svc .circle{position:absolute;left:0;top:0;width:64px;height:64px;border-radius:50%;background:var(--red);display:flex;align-items:center;justify-content:center}
.svc .circle svg{width:32px;height:32px}
.svc h4{position:absolute;left:88px;top:2px;font-family:'Bebas Neue',sans-serif;font-weight:400;font-size:20px;letter-spacing:1.5px;color:var(--white);white-space:nowrap}
.svc p{position:absolute;left:88px;top:30px;width:214px;font-size:11.5px;line-height:18px;color:#e6e6e6}
.svc .more{position:absolute;left:88px;top:104px;font-family:'Bebas Neue',sans-serif;font-size:13px;letter-spacing:1px;color:var(--red)}

/* stats */
.stats{top:2190px;left:124px;width:944px;height:166px;background:var(--white);box-shadow:0 10px 30px rgba(0,0,0,.12)}
.stat{position:absolute;top:28px;display:flex;align-items:center;gap:16px}
.stat svg{width:76px;height:76px}
.stat b{display:block;font-family:'Bebas Neue',sans-serif;font-weight:400;font-size:74px;line-height:66px;color:var(--red)}
.stat span{display:block;font-size:16px;font-weight:600;margin-top:4px}

/* why */
.why .kicker{position:absolute;left:80px;top:2522px}
.why h2{position:absolute;left:80px;top:2554px;font-size:44px}
.why p{position:absolute;left:80px;top:2614px;width:460px;font-size:13.5px;line-height:19.5px;color:var(--text)}

/* testimonials */
.testi{top:2956px;left:0;width:1200px;height:720px;background:linear-gradient(120deg,#0d0e10 0%,#26282b 40%,#4a4c50 65%,#16171a 100%);clip-path:polygon(0 0,100% 44px,100% 93%,0 100%)}
.card{position:absolute;top:3220px;width:264px;height:320px;background:var(--white);text-align:center}
.card .qm{position:absolute;left:14px;top:12px;width:34px;height:26px}
.card .avatar{width:82px;height:82px;border-radius:50%;margin:22px auto 0;background:radial-gradient(circle at 50% 40%,#8a8a8a,#3c3c3c)}
.card h5{font-family:'Tinos',serif;font-size:14px;margin-top:28px}
.card p{font-style:italic;font-size:12.5px;line-height:16px;color:#8a8a8a;width:190px;margin:8px auto 0}
.stars{margin-top:30px;color:var(--star);font-size:20px;letter-spacing:4px}
.arrow{position:absolute;top:3366px;width:20px;height:36px}

/* blog */
.blog-card{position:absolute;top:3928px;width:280px;height:404px;background:var(--white);box-shadow:0 6px 24px rgba(0,0,0,.1)}
.blog-card .img{height:156px;background:linear-gradient(135deg,#1c2230,#48546a 55%,#232a38)}
.blog-card .tag{position:absolute;left:0;top:148px;background:var(--white);padding:6px 14px;font-size:10px;color:var(--red)}
.blog-card h6{position:absolute;left:30px;top:220px;width:220px;font-family:'Bebas Neue',sans-serif;font-weight:400;font-size:19px;line-height:27px;letter-spacing:1.2px;color:#1e2a48}
.blog-card p{position:absolute;left:30px;top:280px;width:220px;font-size:11.5px;line-height:19px;color:#7a7a7a}
.blog-card .more{position:absolute;left:30px;top:356px;font-family:'Bebas Neue',sans-serif;font-size:13px;letter-spacing:1px;color:var(--red)}

/* partners */
.partner{position:absolute;top:4496px;height:20px;border-radius:3px;background:#c8c8c8}

/* footer */
.footer{top:4672px;left:0;width:1200px;height:474px;background:linear-gradient(120deg,#111214 0%,#1e1f22 55%,#2c2d30 100%);clip-path:polygon(0 22px,100% 0,100% 100%,0 100%)}
.brand-foot{top:4784px;left:82px;font-size:70px;line-height:70px;color:#d6d6d6;white-space:nowrap}
.foot-about{top:4876px;left:80px;width:290px;font-size:13px;line-height:19px;color:var(--white)}
.foot-col h3{font-size:27px;color:var(--white)}
.foot-col ul{list-style:none;margin-top:18px}
.foot-col li{font-size:14px;color:var(--white);height:32px;display:flex;align-items:center;gap:12px;white-space:nowrap}
.foot-col li svg{width:14px;height:10px}
.foot-line{top:5040px;left:0;width:1200px;height:1px;background:#3a3a3a}
.foot-small{top:5068px;font-size:13px;color:var(--white)}
</style>
</head>
<body>

<!-- top bar -->
<div class="abs topbar"></div>
<div class="abs topbar-red"></div>
<div class="abs brand-top display">BRIGHTGATE</div>
<div class="abs contact" style="top:14px;left:420px">
  <div class="ico"><svg viewBox="0 0 24 24" width="26" height="26" fill="#fff"><path d="M6.6 10.8a15 15 0 0 0 6.6 6.6l2.2-2.2c.3-.3.7-.4 1-.2 1.1.4 2.3.6 3.6.6.6 0 1 .4 1 1V20c0 .6-.4 1-1 1A17 17 0 0 1 3 4c0-.6.4-1 1-1h3.5c.6 0 1 .4 1 1 0 1.3.2 2.5.6 3.6.1.3 0 .7-.2 1z"/></svg></div>
  <div><small>CALL US</small><span>(555) 014 2280</span></div>
</div>
<div class="abs contact" style="top:14px;left:682px">
  <div class="ico"><svg viewBox="0 0 24 24" width="24" height="24" fill="none" stroke="#fff" stroke-width="2"><rect x="3" y="5" width="18" height="14" rx="1"/><path d="M3 6l9 7 9-7"/></svg></div>
  <div><small>EMAIL US</small><span>HI@BRIGHTGATE.EXAMPLE</span></div>
</div>
<div class="abs social"><i></i><i></i><i></i></div>

<!-- nav -->
<nav class="abs nav">
  <a style="left:50px">HOME</a>
  <a style="left:170px">ABOUT US</a>
  <a style="left:328px">OUR SERVICES</a>
  <a style="left:520px">TESTIMONIALS</a>
  <a style="left:712px">BLOG</a>
  <a style="left:822px">CONTACT</a>
  <div class="search">Search...</div>
</nav>

<!-- hero -->
<section class="abs hero" role="img" aria-label="Mechanic working on a car engine with a wrench, dark workshop photo">
  <h1 class="display">WE ARE QUALIFIED &amp;<br><em>PROFESSIONAL</em></h1>
  <p>Lorem ipsum dolor sit amet, consectetur adipiscing elit, sed do eiusmod tempor incididunt ut labore et dolore magna aliqua. Ut enim ad minim veniam quis nostrud</p>
</section>
<div class="btn" style="left:64px;top:560px;width:184px;height:50px">GET A QUOTE <svg viewBox="0 0 24 24" fill="none" stroke="#fff" stroke-width="2"><circle cx="12" cy="12" r="10"/><path d="M8 12h8M13 8l4 4-4 4"/></svg></div>

<!-- quote form -->
<div class="abs quote">
  <div class="quote-head display">REQUEST A QUOTE</div>
  <div class="field" style="top:108px">FULL NAME</div>
  <div class="field" style="top:190px">EMAIL ADDRESS</div>
  <div class="field" style="top:272px">PHONE NUMBER</div>
  <div class="field area" style="top:356px">ADDITIONAL COMMENT</div>
  <div class="btn" style="left:124px;top:534px;width:186px;height:50px">GET A QUOTE <svg viewBox="0 0 24 24" fill="none" stroke="#fff" stroke-width="2"><circle cx="12" cy="12" r="10"/><path d="M8 12h8M13 8l4 4-4 4"/></svg></div>
</div>

<!-- who we are -->
<section class="who">
  <h2 class="display">WHO WE ARE</h2>
  <p>Lorem ipsum dolor sit amet, consectetur adipiscing elit, sed do eiusmod tempor incididunt ut labore et dolore magna aliqua. Ut enim ad minim veniam, quis nostrud exercitation ullamco laboris nisi ut aliquip ex ea commodo consequat. Duis aute irure dolor in reprehenderit in voluptate velit esse</p>
</section>
<div class="btn" style="left:74px;top:1022px;width:184px;height:50px">READ MORE <svg viewBox="0 0 24 24" fill="none" stroke="#fff" stroke-width="2"><circle cx="12" cy="12" r="10"/><path d="M8 12h8M13 8l4 4-4 4"/></svg></div>

<!-- features -->
<div class="feature" style="left:82px">
  <svg viewBox="0 0 110 110" fill="none" stroke="#c4120f" stroke-width="3"><circle cx="55" cy="34" r="16"/><path d="M37 28h36M44 18q11-8 22 0"/><path d="M22 100V80q0-16 20-20h26q20 4 20 20v20"/><path d="M86 40l-14 14M90 36a6 6 0 1 0-8-2"/></svg>
  <h3 class="display">BEST TECHNICIANS</h3>
  <p>Lorem ipsum dolor sit amet, consectetur adipiscing elit, sed do eiusmod tempor incididunt ut labore et dolore magna aliqua.</p>
</div>
<div class="feature" style="left:428px">
  <svg viewBox="0 0 110 110" fill="none" stroke="#c4120f" stroke-width="3"><circle cx="55" cy="66" r="34"/><circle cx="55" cy="66" r="26"/><path d="M42 80V64h8l8-14q5 0 4 8l-1 6h9q4 1 3 5l-3 11H50"/><path d="M20 16l3 6 6 1-5 4 1 6-5-3-5 3 1-6-5-4 6-1zM55 6l3 6 6 1-5 4 1 6-5-3-5 3 1-6-5-4 6-1zM90 16l3 6 6 1-5 4 1 6-5-3-5 3 1-6-5-4 6-1z"/></svg>
  <h3 class="display">QUALITY SERVICES</h3>
  <p>Lorem ipsum dolor sit amet, consectetur adipiscing elit, sed do eiusmod tempor incididunt ut labore et dolore magna aliqua.</p>
</div>
<div class="feature" style="left:778px">
  <svg viewBox="0 0 110 110" fill="none" stroke="#c4120f" stroke-width="3"><circle cx="68" cy="28" r="18"/><circle cx="68" cy="28" r="11"/><path d="M68 22v12M64 25h8M64 31h8"/><path d="M10 80l16-14q10-6 22-2l18 4q6 2 3 8H46"/><path d="M69 76l22-12q9-2 6 6L66 94H30l-14 8"/></svg>
  <h3 class="display">AFFORDABLE PRICES</h3>
  <p>Lorem ipsum dolor sit amet, consectetur adipiscing elit, sed do eiusmod tempor incididunt ut labore et dolore magna aliqua.</p>
</div>

<!-- services -->
<section class="abs services" role="img" aria-label="Dark close-up photo of a car engine bay">
  <div class="abs kicker display" style="top:104px;left:0;width:1200px;text-align:center;font-size:18px;letter-spacing:1.5px">OUR SERVICES</div>
  <h2 class="abs sec-title display" style="top:132px;left:0;width:1200px;text-align:center;color:#fff">GREAT CAR SERVICES</h2>
</section>
<div class="svc" style="left:126px;top:1810px"><div class="circle"><svg viewBox="0 0 32 32" fill="none" stroke="#fff" stroke-width="2"><circle cx="16" cy="11" r="6"/><path d="M10 9h12M6 28v-4q0-6 7-7h6q7 1 7 7v4"/></svg></div><h4>TECHNICAL REPAIRS</h4><p>Lorem ipsum dolor sit amet, consect adipiscing elit, sed do eiusmod tempor incididunt ut labore</p><span class="more">READ MORE &#8594;</span></div>
<div class="svc" style="left:446px;top:1810px"><div class="circle"><svg viewBox="0 0 32 32" fill="none" stroke="#fff" stroke-width="2"><path d="M6 6l20 20M26 6L6 26"/><circle cx="6" cy="6" r="3"/><circle cx="26" cy="6" r="3"/></svg></div><h4>ENGINE DIAGNOSTICS</h4><p>Lorem ipsum dolor sit amet, consect adipiscing elit, sed do eiusmod tempor incididunt ut labore</p><span class="more">READ MORE &#8594;</span></div>
<div class="svc" style="left:764px;top:1810px"><div class="circle"><svg viewBox="0 0 32 32" fill="none" stroke="#fff" stroke-width="2"><path d="M8 24l12-12M22 4a6 6 0 1 0 6 6l-4 1-3-3z"/><path d="M6 6l8 8"/></svg></div><h4>SYSTEM SERVICE</h4><p>Lorem ipsum dolor sit amet, consect adipiscing elit, sed do eiusmod tempor incididunt ut labore</p><span class="more">READ MORE &#8594;</span></div>
<div class="svc" style="left:126px;top:1980px"><div class="circle"><svg viewBox="0 0 32 32" fill="none" stroke="#fff" stroke-width="2"><path d="M4 6h24L18 18v9l-4-2v-7z"/></svg></div><h4>OIL AND FILTERS</h4><p>Lorem ipsum dolor sit amet, consect adipiscing elit, sed do eiusmod tempor incididunt ut labore</p><span class="more">READ MORE &#8594;</span></div>
<div class="svc" style="left:446px;top:1980px"><div class="circle"><svg viewBox="0 0 32 32" fill="none" stroke="#fff" stroke-width="2"><circle cx="16" cy="16" r="12"/><circle cx="16" cy="16" r="5"/><path d="M16 4v7M16 21v7M4 16h7M21 16h7"/></svg></div><h4>TIRES AND WHEELS</h4><p>Lorem ipsum dolor sit amet, consect adipiscing elit, sed do eiusmod tempor incididunt ut labore</p><span class="more">READ MORE &#8594;</span></div>
<div class="svc" style="left:764px;top:1980px"><div class="circle"><svg viewBox="0 0 32 32" fill="none" stroke="#fff" stroke-width="2"><circle cx="16" cy="16" r="12"/><path d="M18 7l-6 10h6l-4 8"/></svg></div><h4>ELECTRICAL SYSTEM</h4><p>Lorem ipsum dolor sit amet, consect adipiscing elit, sed do eiusmod tempor incididunt ut labore</p><span class="more">READ MORE &#8594;</span></div>

<!-- stats -->
<div class="abs stats">
  <div class="stat" style="left:52px"><svg viewBox="0 0 76 76" fill="none" stroke="#c4120f" stroke-width="2.5"><circle cx="38" cy="22" r="10"/><circle cx="16" cy="34" r="7"/><circle cx="60" cy="34" r="7"/><path d="M22 70V50q0-12 16-12t16 12v20M4 70V56q0-8 12-8M72 70V56q0-8-12-8"/></svg><div><b>1K+</b><span>HAPPY CLIENTS</span></div></div>
  <div class="stat" style="left:336px"><svg viewBox="0 0 76 76" fill="none" stroke="#c4120f" stroke-width="2.5"><circle cx="38" cy="38" r="26"/><circle cx="38" cy="38" r="12"/><path d="M38 4v8M38 64v8M4 38h8M64 38h8M14 14l6 6M56 56l6 6M62 14l-6 6M14 62l6-6"/></svg><div><b>2K+</b><span>CAR REPAIRED</span></div></div>
  <div class="stat" style="left:626px"><svg viewBox="0 0 76 76" fill="none" stroke="#c4120f" stroke-width="2.5"><circle cx="38" cy="38" r="32"/><circle cx="38" cy="38" r="22"/><circle cx="38" cy="38" r="6"/><path d="M38 16v16M38 44v16M16 38h16M44 38h16"/></svg><div><b>5K+</b><span>TYRES REPLACED</span></div></div>
</div>

<!-- why choose us -->
<section class="why">
  <div class="kicker">WHY CHOOSE US</div>
  <h2 class="display">WE ARE QUALIFIED</h2>
  <p>Lorem ipsum dolor sit amet, consectetur adipiscing elit, sed do eiusmod tempor incididunt ut labore et dolore magna aliqua. Ut enim ad minim veniam, quis nostrud exercitation ullamco laboris nisi ut aliquip ex ea commodo consequat. Duis aute irure dolor in reprehenderit in voluptate velit esse</p>
</section>
<div class="btn" style="left:84px;top:2742px;width:186px;height:48px">GET A QUOTE <svg viewBox="0 0 24 24" fill="none" stroke="#fff" stroke-width="2"><circle cx="12" cy="12" r="10"/><path d="M8 12h8M13 8l4 4-4 4"/></svg></div>
<div class="photo" style="left:594px;top:2500px;width:504px;height:310px;background:linear-gradient(135deg,#2a2d33,#6d727b 50%,#1e2026)" role="img" aria-label="Gloved mechanic's hand working in a car engine bay"></div>

<!-- testimonials -->
<section class="abs testi" role="img" aria-label="Dark workshop photo of a mechanic under a car">
  <div class="abs kicker" style="top:104px;left:0;width:1200px;text-align:center">TESTIMONIALS</div>
  <h2 class="abs sec-title display" style="top:138px;left:0;width:1200px;text-align:center;color:#fff">HAPPY CUSTOMERS</h2>
</section>
<svg class="arrow" style="left:84px" viewBox="0 0 20 36" fill="none" stroke="#fff" stroke-width="2.5"><path d="M16 4L4 18l12 14"/></svg>
<svg class="arrow" style="left:1098px" viewBox="0 0 20 36" fill="none" stroke="#fff" stroke-width="2.5"><path d="M4 4l12 14L4 32"/></svg>
<div class="card" style="left:158px"><svg class="qm" viewBox="0 0 34 26" fill="#c4120f"><path d="M0 0h14v14l-6 12H2l5-12H0zM20 0h14v14l-6 12h-6l5-12h-7z"/></svg><div class="avatar" role="img" aria-label="Customer portrait"></div><h5>DALE MORROW</h5><p>Lorem ipsum dolor sit amet, consectetuer adipiscing elit, sed diam nonummy nibh euismod tincidunt ut laoreet dolore magna aliquam</p><div class="stars">★★★★★</div></div>
<div class="card" style="left:466px"><svg class="qm" viewBox="0 0 34 26" fill="#c4120f"><path d="M0 0h14v14l-6 12H2l5-12H0zM20 0h14v14l-6 12h-6l5-12h-7z"/></svg><div class="avatar" role="img" aria-label="Customer portrait"></div><h5>KT HARLAN</h5><p>Lorem ipsum dolor sit amet, consectetuer adipiscing elit, sed diam nonummy nibh euismod tincidunt ut laoreet dolore magna aliquam</p><div class="stars">★★★★★</div></div>
<div class="card" style="left:774px"><svg class="qm" viewBox="0 0 34 26" fill="#c4120f"><path d="M0 0h14v14l-6 12H2l5-12H0zM20 0h14v14l-6 12h-6l5-12h-7z"/></svg><div class="avatar" role="img" aria-label="Customer portrait"></div><h5>RENI A CALDER</h5><p>Lorem ipsum dolor sit amet, consectetuer adipiscing elit, sed diam nonummy nibh euismod tincidunt ut laoreet dolore magna aliquam</p><div class="stars">★★★★★</div></div>

<!-- blog -->
<div class="abs kicker" style="top:3760px;left:0;width:1200px;text-align:center">NEWS</div>
<h2 class="abs sec-title display" style="top:3796px;left:0;width:1200px;text-align:center">LATEST FROM BLOG</h2>
<article class="blog-card" style="left:174px"><div class="img" role="img" aria-label="Mechanic leaning over an open car engine"></div><span class="tag">Maintenance</span><h6>HOW OFTEN SHOULD YOU DETAIL YOUR CAR</h6><p>Lorem ipsum dolor sit amet, consectetur adipiscing elit, sed do eiusmod tempor incididunt ut...</p><span class="more">READ MORE &#8594;</span></article>
<article class="blog-card" style="left:478px"><div class="img" role="img" aria-label="Two mechanics working on an engine"></div><span class="tag">Engine Care</span><h6>DETAILING YOUR CAR FOR SPECIAL OCCASIONS</h6><p>Lorem ipsum dolor sit amet, consectetur adipiscing elit, sed do eiusmod tempor incididunt ut...</p><span class="more">READ MORE &#8594;</span></article>
<article class="blog-card" style="left:782px"><div class="img" role="img" aria-label="Mechanic checking a car engine"></div><span class="tag">Engine Care</span><h6>THE POWER OF A PROPER TUNE UP ON CAR</h6><p>Lorem ipsum dolor sit amet, consectetur adipiscing elit, sed do eiusmod tempor incididunt ut...</p><span class="more">READ MORE &#8594;</span></article>

<!-- partners -->
<div class="partner" style="left:204px;width:86px"></div>
<div class="partner" style="left:340px;width:94px"></div>
<div class="partner" style="left:486px;width:86px"></div>
<div class="partner" style="left:622px;width:96px"></div>
<div class="partner" style="left:766px;width:94px"></div>
<div class="partner" style="left:902px;width:108px"></div>

<!-- footer -->
<footer class="abs footer" role="img" aria-label="Dark workshop background photo"></footer>
<div class="abs brand-foot display">BRIGHTGATE</div>
<p class="abs foot-about">Lorem ipsum dolor sit amet, consectetur adipiscing elit, sed do eiusmod tempor.</p>
<div class="abs foot-col" style="left:388px;top:4778px"><h3 class="display">QUICK LINKS</h3><ul>
  <li><svg viewBox="0 0 14 10" fill="none" stroke="#c4120f" stroke-width="1.6"><path d="M0 5h12M8 1l4 4-4 4"/></svg>HOME</li>
  <li><svg viewBox="0 0 14 10" fill="none" stroke="#c4120f" stroke-width="1.6"><path d="M0 5h12M8 1l4 4-4 4"/></svg>ABOUT</li>
  <li><svg viewBox="0 0 14 10" fill="none" stroke="#c4120f" stroke-width="1.6"><path d="M0 5h12M8 1l4 4-4 4"/></svg>SERVICES</li>
  <li><svg viewBox="0 0 14 10" fill="none" stroke="#c4120f" stroke-width="1.6"><path d="M0 5h12M8 1l4 4-4 4"/></svg>TESTIMONIALS</li>
  <li><svg viewBox="0 0 14 10" fill="none" stroke="#c4120f" stroke-width="1.6"><path d="M0 5h12M8 1l4 4-4 4"/></svg>CONTACT</li>
</ul></div>
<div class="abs foot-col" style="left:588px;top:4778px"><h3 class="display">OUR SERVICES</h3><ul>
  <li><svg viewBox="0 0 14 10" fill="none" stroke="#c4120f" stroke-width="1.6"><path d="M0 5h12M8 1l4 4-4 4"/></svg>TECHNICAL REPAIRD</li>
  <li><svg viewBox="0 0 14 10" fill="none" stroke="#c4120f" stroke-width="1.6"><path d="M0 5h12M8 1l4 4-4 4"/></svg>OIL &amp; FILTERS</li>
  <li><svg viewBox="0 0 14 10" fill="none" stroke="#c4120f" stroke-width="1.6"><path d="M0 5h12M8 1l4 4-4 4"/></svg>TIRES AND WHEELS</li>
  <li><svg viewBox="0 0 14 10" fill="none" stroke="#c4120f" stroke-width="1.6"><path d="M0 5h12M8 1l4 4-4 4"/></svg>ELECTRICAL SYSTEMS</li>
  <li><svg viewBox="0 0 14 10" fill="none" stroke="#c4120f" stroke-width="1.6"><path d="M0 5h12M8 1l4 4-4 4"/></svg>ENGINES REPAIRS</li>
</ul></div>
<div class="abs foot-col" style="left:854px;top:4778px"><h3 class="display">OPENING HOURS</h3><ul>
  <li>MONDAY – FRIDAY , 8 AM – 7 PM</li>
  <li>SATURDAY, CLOSED</li>
  <li>SUNDAY, CLOSED</li>
</ul></div>
<div class="abs foot-line"></div>
<div class="abs foot-small" style="left:84px">Car Repair &amp; Auto Service</div>
<div class="abs foot-small" style="left:896px">Privacy Policy- Terms &amp; Conditions</div>

</body>
</html>
```